Retail Jewelry Business Card Design Project

We are in need of a new business card design for a retail jewelry store. This store is in the business of fine jewelry including but not specific to bridal jewelry, diamonds, designer jewelry and watches.

This store has been in business for 20 years but continues to strive for a modern professional appeal. The main colors use for this business are a royal blue, white and silver.

Target Market(s)

Target market is ages 18-50

Industry/Entity Type

Jewelry

Requirements
Must have
• Sales Person Name
Sales Person Email Address

Store Address
Store Phone
Website

Standard business card size. No odd shapes or sizes.
Nice to have
• Overall modern feel for card.

We have thought that a design with a nice feature of the logo on the back of the card would be nice but open to ideas.
Should not have
• No specific images of jewelry should be used.

```html
<!DOCTYPE html>
<html lang="en">
<head>
<meta charset="utf-8">
<title>Harlow Reid Fine Jewelry – Business Card</title>
<link rel="stylesheet" href="https://fonts.googleapis.com/css2?family=Courier+Prime:wght@400;700&display=swap">
<style>
  :root {
    --stage: #3aa6f0;
    --card-front: #999999;
    --card-back: #161616;
    --royal-blue: #1a1ae6;
    --white: #ffffff;
    --silver: #b9b9b9;
    --type: "Courier Prime", "Courier New", monospace;
  }
  * { margin: 0; padding: 0; box-sizing: border-box; }
  html, body { width: 1200px; height: 1003px; overflow: hidden; }
  body {
    background: var(--stage);
    font-family: var(--type);
    position: relative;
  }
  .card {
    position: absolute;
    width: 500px;
    height: 305px;
    top: 349px;
    box-shadow: 0 4px 10px rgba(0,0,0,0.35);
  }
  .card--front { left: 70px; background: var(--card-front); color: var(--white); }
  .card--back { left: 630px; background: var(--card-back); }

  .brand {
    position: absolute;
    font-family: var(--type);
    font-weight: 700;
    text-align: center;
    line-height: 1.05;
  }
  .card--front .brand {
    right: 36px; top: 26px; width: 250px;
    color: var(--royal-blue);
    font-size: 30px;
  }
  .brand__sub { display: block; font-size: 15px; letter-spacing: 2px; margin-top: 6px; }

  .person {
    position: absolute; left: 30px; top: 100px;
    font-weight: 700; font-size: 19px; line-height: 1.35;
  }
  .person__phone {
    position: absolute; left: 32px; top: 178px;
    font-size: 19px;
  }
  .store {
    position: absolute; left: 218px; top: 136px;
    font-size: 14px; line-height: 1.35;
  }
  .contacts {
    position: absolute; left: 218px; top: 210px;
    list-style: none; font-size: 14px; line-height: 1.3;
  }
  .contacts li { display: flex; align-items: center; gap: 8px; }
  .contacts svg { width: 12px; height: 12px; fill: var(--white); flex: none; }
  .contacts .web { font-weight: 700; }

  .back__pattern {
    position: absolute; inset: 0;
    background: linear-gradient(135deg, #1f1f1f, #0e0e0e);
  }
  .card--back .brand {
    left: 0; right: 0; top: 108px;
    color: var(--silver);
    font-size: 46px;
  }
  .card--back .brand__sub { font-size: 20px; letter-spacing: 3px; margin-top: 10px; }
</style>
</head>
<body>

<section class="card card--front" aria-label="Business card front">
  <div class="brand">Harlow Reid<span class="brand__sub">FINE JEWELRY</span></div>

  <div class="person">Harlow Reid<br>Pemberton</div>
  <div class="person__phone">555 010 2468</div>

  <address class="store" style="font-style:normal">
    Harlow Reid Fine<br>
    2280 Linden Avenue<br>
    Bayport, FL 32000
  </address>

  <ul class="contacts">
    <li>
      <svg viewBox="0 0 12 12" aria-hidden="true"><path d="M1 4 Q6 0 11 4 L9 5 L8 4 Q6 3 4 4 L3 5 Z M2 6 H10 V11 H2 Z"/></svg>
      +(0) 55 01 23 410
    </li>
    <li>
      <svg viewBox="0 0 12 12" aria-hidden="true"><path d="M3 1 H9 V4 H3 Z M1 5 H11 V10 H1 Z"/></svg>
      +(0) 55 01 23 411
    </li>
    <li>
      <svg viewBox="0 0 12 12" aria-hidden="true"><path d="M1 2 H11 V10 H1 Z M1.5 2.5 L6 6.5 L10.5 2.5" stroke="#999" stroke-width="1"/></svg>
      harlow@harlowreidjewelry.com
    </li>
    <li class="web">
      <svg viewBox="0 0 12 12" aria-hidden="true"><circle cx="6" cy="6" r="5.5"/><path d="M0.5 6 H11.5 M6 0.5 V11.5" stroke="#999" stroke-width="0.8"/></svg>
      www.harlowreidjewelry.com
    </li>
  </ul>
</section>

<section class="card card--back" aria-label="Business card back">
  <div class="back__pattern" role="img" aria-label="Subtle dark repeating fleur-de-lis pattern"></div>
  <div class="brand">Harlow Reid<span class="brand__sub">FINE JEWELRY</span></div>
</section>

</body>
</html>
```